Lounge Bar Menu

We need an elegant Bar Menu for ou Lounge Bar.
Logo attached.
We already have the support. A cover like a book in A5 format.
Attached as well our menu.

Industry/Entity Type

Bar, Hotel4*

```html
<!DOCTYPE html>
<html lang="fr">
<head>
<meta charset="utf-8">
<title>Velour Lounge-Bar — Carte</title>
<link href="https://fonts.googleapis.com/css2?family=Marcellus&family=Kaushan+Script&display=swap" rel="stylesheet">
<style>
  :root {
    --bg: #000000;
    --ink: #f1f1ee;
    --gold: #c9a262;
    --olive: #9ba41b;
    --glass-a: #2a2a2a;
    --glass-b: #111111;
  }
  * { margin: 0; padding: 0; box-sizing: border-box; }
  html, body { width: 839px; height: 1200px; overflow: hidden; background: var(--bg); }
  .menu {
    position: relative; width: 839px; height: 1200px; overflow: hidden;
    background: var(--bg); color: var(--ink);
    font-family: "Marcellus", serif;
  }
  .illustration { position: absolute; }
  .illustration--coupe {
    left: 625px; top: 30px; width: 192px; height: 332px;
    background: radial-gradient(ellipse at 50% 30%, var(--glass-a), var(--glass-b) 70%, transparent 100%);
    border-radius: 50% 50% 30% 30% / 40% 40% 10% 10%;
  }
  .illustration--balloon {
    left: 473px; top: 716px; width: 344px; height: 466px;
    background: radial-gradient(ellipse at 55% 40%, var(--glass-a), var(--glass-b) 70%, transparent 100%);
    border-radius: 48% 48% 20% 20% / 40% 40% 8% 8%;
  }
  .brand { position: absolute; left: 78px; top: 44px; }
  .brand__name { font-size: 56px; line-height: 64px; color: var(--gold); }
  .brand__tag { font-size: 17px; line-height: 24px; margin-top: 6px; color: var(--ink); }
  .heading {
    position: absolute; left: 78px; font-family: "Kaushan Script", cursive;
    color: var(--olive); font-size: 27px; line-height: 34px; white-space: nowrap; font-weight: 400;
  }
  .line { position: absolute; font-size: 17.2px; line-height: 24px; white-space: nowrap; }
  .line--item { left: 77px; }
  .line--item::before { content: "-"; display: inline-block; width: 17px; }
  .line--deco { left: 146px; }
  .line--plain { left: 77px; }
</style>
</head>
<body>
<main class="menu">
  <div class="illustration illustration--coupe" role="img" aria-label="Dessin à la craie d'une coupe à cocktail garnie d'une cerise"></div>
  <div class="illustration illustration--balloon" role="img" aria-label="Dessin à la craie d'un verre ballon avec glaçons, rondelle d'agrume et paille"></div>

  <header class="brand">
    <div class="brand__name">Velour</div>
    <div class="brand__tag">Lounge - Bar</div>
  </header>

  <h2 class="heading" style="top:186px">Cocktail avec alcool : 14 euros</h2>
  <p class="line line--item" style="top:246px">Aglio : gin- lissé rosé-vermouth blanc et dry infusé à l’ail- Bitter citron</p>
  <p class="line line--item" style="top:270px">Amaretto Sour Arancia : Amaretto- jus de citron-jus d’orange frais-Costura Bitter</p>
  <p class="line line--item" style="top:294px">Americano by Velour : Cardelli- eaux gazeuse- vermouth rouge à la cardamome</p>
  <p class="line line--item" style="top:318px">Bronx : Gin- jus d’orange frais- vermouth blanc- vermouth rouge</p>
  <p class="line line--item" style="top:342px">Famous negroni : Gin- vermouth rouge- saumur-cardelli-capres</p>
  <p class="line line--item" style="top:366px">Infinite Velour : Cognac-Rovarotti- sirop simple- peyroux bitter</p>
  <p class="line line--item" style="top:390px">Limoncello Sour : limoncello-shrub Agrume- Bitter citron- jus de citron</p>
  <p class="line line--item" style="top:414px">Tomatini : Vodka-tomate cerise-vinaigre blanc balsamique-jus citron-vermouth blanc</p>
  <p class="line line--item" style="top:438px">Word rye : Mezcal- Aperitivo-amaretto- orange bitter</p>

  <h2 class="heading" style="top:489px">Cocktail sans alcool :10 euros</h2>
  <p class="line line--item" style="top:548px">Le Velour :  Bitter san Varino-jus de clementine-jus de citron-sirop de sucre</p>
  <p class="line line--deco" style="top:572px">Déco : une branche de romarin</p>
  <p class="line line--item" style="top:621px">Spritz sans alcool : Bitter san Varino-perlière-top de limonade</p>
  <p class="line line--deco" style="top:645px">Déco : rondelle d’orange et tete de menthe</p>
  <p class="line line--item" style="top:693px">Twist shirley temple : sirop de grenadine-jus de citron-top de ginger beer</p>
  <p class="line line--deco" style="top:717px">Déco : brochette de 3 cerise Amarena</p>
  <p class="line line--item" style="top:765px">Suvane tonic sans alcool 7 euros</p>

  <h2 class="heading" style="top:819px">Eaux :</h2>
  <p class="line line--plain" style="top:854px">&nbsp;Acqua Velia/ San Varino &nbsp;&nbsp;25cl 3 euros /75cl 7 euros</p>
  <p class="line line--plain" style="top:878px">Perlière 33cl 4.50 euros</p>

  <h2 class="heading" style="top:914px">Soft :4.50 euros</h2>
  <p class="line line--plain" style="top:949px">Kola/kola zero 33cl</p>
  <p class="line line--plain" style="top:973px">Oranjette 33cl</p>
  <p class="line line--plain" style="top:997px">Swanley tonic 33cl</p>
  <p class="line line--plain" style="top:1021px">Ice tea breeze tea</p>
  <p class="line line--plain" style="top:1045px">Limonade LMP</p>
  <p class="line line--plain" style="top:1069px">Bitter san varino</p>
  <p class="line line--plain" style="top:1093px">Ember Leaf ginger beer 20 cl 6 euros</p>
  <p class="line line--plain" style="top:1117px">Ember Leaf tonic 20 cl 6 euros</p>
</main>
</body>
</html>
```